Velmor PashuのRTZの電子書籍表紙デザインをお願いします。

*週末ごとに和みを探す読者へ贈る癒やしの四季手帳*というタイトルの表紙デザインの発注です。
サブタイトル 猫の昼寝は街を照らす
猫の昼寝は毎日を照らす
私は猫の昼寝に癒された
になります。
お笑い要素の多い1日1笑いみたいな本の表紙です。

初めての表紙デザイン依頼なので、よく勝手がわかっていませんので、
出来上がったデザインを作家グループの中で投票にかけて、
一番投票得票数の多かったものを表紙デザインとして選ばせていただきたいと考えております。
もしかしたら、その中で、何か修正依頼など来るかもしれませんが、
それも含めて、ご対応していただける方よろしくお願いします。

1部内容の抜粋を記載します。

その他何かご不明な点がございましたら、お気軽にご質問下さい。
よろしくお願いいたします。
すいません。作家名は後でお伝えします。作家名もどこかに挿入いただきたいです。よろしくお願いします。
データサイズですが、推奨サイズでJPEGファイルでご納品下さい、よろしくお願いします。
皆様、たくさんのご応募まことにありがとうございました。
現在、作家グループへ全体回覧のメールを致しました。
皆様の投票結果までお待ちください。
また、この度、いろいろな作品に触れさせていただきましたこと本当に
本当に感謝いたします。
今回の表紙に関しましては、どうしても1名しか選べない状況がございますこと
また、選挙による投票にて決定致しますこと、ご理解何卒よろしくお願い申しあげます。
また、もしも、今回当選に至らないことがありましても、
今後も私自身は作家生活を継続予定ですので、
(今回は作品の表紙に合わないことがあっても)作風の気に入ったデザイナー様には
個人的にお話を相談させていただく場合もあると思っております。
その際には何卒よろしくお願い申し上げます。この度はまことにありがとうございました。
この度はご応募まことにありがとうございました。厳選なる選挙の結果、1名の作家さんが選ばれました。
選ばれました方には個別にお伝えいたしております。この度はまことにご応募ありがとうございました。

作家メンバーによる総選挙にて決定させて頂きました。皆様に広く愛される作品で、投票数も多く選ばせて頂きました。誠にありがとうございました。

今回、誠にご提案ありがとうございました。私自身は作家活動を継続していくつもりですので、また、個別にご依頼させて頂くこともあるかと思います。その時はよろしくお願いします。この度はありがとうございました。

```html
<!DOCTYPE html>
<html lang="ja">
<head>
<meta charset="utf-8">
<title>週末ごとに和みを探す読者へ贈る癒やしの四季手帳</title>
<link href="https://fonts.googleapis.com/css2?family=Noto+Sans+JP:wght@500;700;900&display=swap" rel="stylesheet">
<style>
  :root {
    --frame: #f7d21c;
    --paper: #ffffff;
    --ink: #1a1a1a;
    --smile: #f7d21c;
    --curl: #c9c9c9;
    --curl-shade: #9e9e9e;
  }
  html, body { margin: 0; padding: 0; overflow: hidden; }
  body { width: 750px; height: 1200px; background: var(--frame); font-family: "Noto Sans JP", sans-serif; color: var(--ink); }
  .cover { position: relative; width: 750px; height: 1200px; overflow: hidden; }
  .page { position: absolute; left: 40px; top: 40px; width: 670px; height: 1120px; background: var(--paper); }
  .shapes { position: absolute; left: 0; top: 0; }
  .lead { position: absolute; left: 262px; top: 78px; margin: 0; font-size: 27px; font-weight: 900; letter-spacing: 0; white-space: nowrap; }
  .title { position: absolute; margin: 0; font-weight: 900; line-height: 1; white-space: nowrap; }
  .title-1 { left: 185px; top: 170px; font-size: 150px; letter-spacing: -4px; }
  .title-2 { left: 215px; top: 340px; font-size: 124px; letter-spacing: -2px; }
  .title-3 { left: 100px; top: 480px; font-size: 124px; letter-spacing: -2px; }
  .bubble-text { position: absolute; margin: 0; font-weight: 700; text-align: center; line-height: 1.3; white-space: nowrap; transform: translate(-50%, -50%); }
  .bubble-life { left: 170px; top: 128px; font-size: 24px; }
  .bubble-town { left: 562px; top: 622px; font-size: 24px; }
  .bubble-healed { left: 165px; top: 940px; font-size: 23px; }
  .author { position: absolute; left: 290px; top: 1040px; display: flex; align-items: flex-end; gap: 28px; }
  .author-label { font-size: 30px; font-weight: 700; margin-bottom: 4px; }
  .author-names { display: flex; flex-direction: column; }
  .author-reading { font-size: 18px; font-weight: 500; letter-spacing: 3px; }
  .author-name { font-size: 38px; font-weight: 900; letter-spacing: 2px; }
</style>
</head>
<body>
<main class="cover">
  <div class="page"></div>

  <svg class="shapes" width="750" height="1200" viewBox="0 0 750 1200">
    <!-- bubble: daily -->
    <g fill="#ffffff" stroke="#1a1a1a" stroke-width="4">
      <path d="M115 168 L100 205 L150 175 Z"/>
      <ellipse cx="170" cy="125" rx="95" ry="55"/>
      <path d="M117 166 L150 173" stroke="#ffffff" stroke-width="6"/>
    </g>
    <!-- bubble: town -->
    <g fill="#ffffff" stroke="#1a1a1a" stroke-width="4">
      <path d="M500 665 L470 705 L530 675 Z"/>
      <ellipse cx="562" cy="620" rx="108" ry="60"/>
      <path d="M502 664 L530 672" stroke="#ffffff" stroke-width="6"/>
    </g>
    <!-- bubble around the smile mark -->
    <g fill="#ffffff" stroke="#1a1a1a" stroke-width="4">
      <path d="M340 895 L300 935 L370 905 Z"/>
      <ellipse cx="400" cy="828" rx="112" ry="94"/>
      <path d="M342 893 L370 903" stroke="#ffffff" stroke-width="6"/>
    </g>
    <circle cx="400" cy="826" r="62" fill="var(--smile)" role="img" aria-label="笑顔のマーク"/>
    <!-- bubble: healed -->
    <g fill="#ffffff" stroke="#1a1a1a" stroke-width="4">
      <path d="M230 985 L265 1020 L215 998 Z"/>
      <ellipse cx="165" cy="938" rx="102" ry="72"/>
      <path d="M228 984 L215 996" stroke="#ffffff" stroke-width="6"/>
    </g>
    <!-- page curl -->
    <path d="M40 1090 L40 1160 L110 1160 Z" fill="var(--frame)"/>
    <path d="M40 1090 Q70 1110 110 1160 L85 1125 Z" fill="var(--curl)"/>
    <path d="M40 1090 L110 1160 Q60 1150 40 1090 Z" fill="var(--curl-shade)"/>
  </svg>

  <p class="lead">週末ごとに和みを探す読者へ贈る</p>
  <h1 class="title title-1">癒やし</h1>
  <p class="title title-2">の四季</p>
  <p class="title title-3">手帳</p>

  <p class="bubble-text bubble-life">猫の昼寝は<br>毎日を照らす</p>
  <p class="bubble-text bubble-town">猫の昼寝は<br>街を照らす</p>
  <p class="bubble-text bubble-healed">私は<br>猫の昼寝に<br>癒された</p>

  <div class="author">
    <span class="author-label">著者</span>
    <div class="author-names">
      <span class="author-reading">ベルモア・パシュ</span>
      <span class="author-name">Velmor Pashu</span>
    </div>
  </div>
</main>
</body>
</html>
```